Upscale business cards needed for Board of Directors

We need professional business cards created for members of our family business Board of Directors. We would like these relatively simple and straightforward, but also with a unique element to set them apart. Probably stick with neutral and simple colors - white, grey etc. We need space for the traditional elements, including name, title, address, email/phone number. And we will be creating several from this template so it needs to be template that is easy to switch information in and out of.
Business
See description

```html
<!DOCTYPE html>
<html lang="en">
<head>
<meta charset="utf-8">
<title>Keelstone Holdings – Business Card</title>
<link rel="stylesheet" href="https://fonts.googleapis.com/css2?family=Tinos:wght@400;700&display=swap">
<style>
  :root {
    --page: #ffffff;
    --card: #2b2b2b;
    --card-edge: #1f1f1f;
    --gold: #c8955a;
    --gold-light: #e0b98a;
    --ink-light: #e9e2d8;
  }
  * { margin: 0; padding: 0; box-sizing: border-box; }
  html, body {
    width: 1200px;
    height: 1000px;
    overflow: hidden;
    background: var(--page);
  }
  .canvas {
    position: relative;
    width: 1200px;
    height: 1000px;
    font-family: "Tinos", "Times New Roman", serif;
  }
  .card {
    position: absolute;
    width: 464px;
    height: 269px;
    background: var(--card);
    border: 1px solid var(--card-edge);
  }
  .card--front { left: 110px; top: 243px; }
  .card--back  { left: 599px; top: 413px; }

  .brand-name {
    position: absolute;
    color: var(--gold);
    font-weight: 700;
    text-transform: uppercase;
    text-align: center;
    white-space: nowrap;
  }
  .brand-name__line { display: block; }
  .card--front .brand-name {
    left: 0; right: 0;
    top: 100px;
    font-size: 27px;
    line-height: 31px;
    letter-spacing: 2px;
  }
  .card--back .brand-name {
    left: 252px;
    width: 180px;
    top: 34px;
    font-size: 20px;
    line-height: 24px;
    letter-spacing: 1.5px;
  }

  .person {
    position: absolute;
    left: 54px;
    top: 32px;
  }
  .person__name {
    color: var(--gold-light);
    font-size: 21px;
    font-weight: 700;
    letter-spacing: 0.5px;
    white-space: nowrap;
  }
  .person__title {
    color: var(--gold);
    font-size: 11px;
  }
  .person__rule {
    width: 53px;
    height: 2px;
    background: var(--gold);
    margin-top: 15px;
  }

  .contact {
    position: absolute;
    left: 54px;
    top: 178px;
    font-size: 12.5px;
    line-height: 16px;
    white-space: nowrap;
  }
  .contact__phone { color: var(--ink-light); }
  .contact__email { color: var(--gold-light); }
  .contact__web { color: var(--gold-light); margin-top: 13px; }
</style>
</head>
<body>
<main class="canvas">
  <section class="card card--front" aria-label="Card front">
    <div class="brand-name">
      <span class="brand-name__line">Keelstone</span>
      <span class="brand-name__line">Holdings</span>
    </div>
  </section>

  <section class="card card--back" aria-label="Card back">
    <div class="person">
      <div class="person__name">Daniel Mercer</div>
      <div class="person__title">Manager</div>
      <div class="person__rule"></div>
    </div>
    <div class="brand-name">
      <span class="brand-name__line">Keelstone</span>
      <span class="brand-name__line">Holdings</span>
    </div>
    <div class="contact">
      <div class="contact__phone">+91 900-412-7765</div>
      <div class="contact__email">support@keelstoneholdings.com</div>
      <div class="contact__web">www.KeelstoneHoldings.com</div>
    </div>
  </section>
</main>
</body>
</html>
```